依頼詳細
・企業サイトですが、かたくならず、面白さがほしいです。
・コンテンツ内容は「ごあいさつ」「会社案内」「製品案内」「採用情報」「お問い合わせ」となる予定です。
・TOPページにはスライドショーもしくはそれに変わるものを最初に配置して下さい。
・TOPページと、下層ページのデザインをお願いします。
・TOPページにはNEWS(お知らせ)欄が入る予定です。
・最終的に当方でWordPressにて構築します。
・既存サイトのイメージにとらわれない自由なデザインでもOKです。
ぜひ様々なアイデアをご提案下さい。
サイトURL
http://www.kenro-gear.jp/
ページ数
2ページ
希望イメージ
• +5 0 +5
• シンプル
複雑
• 単色
カラフル
• 暗い
明るい
• 日常
高級
• 遊び心
厳粛
• 未来的
伝統的
• 女性的
男性的
希望する色
青系、グレー系、カラーリングは、添付のロゴマークにある色をベースに考えて頂くと望ましいです。
納品ファイル
• 高解像度JPG (.jpg)
• イラストレーター形式 (.ai)
• フォトショップ形式 (.psd)
補足説明
素材画像で購入が必要なものがある場合、「Pixaveno Media (https://media.pixaveno.com/jp/)」より選定下さい。当方で購入しますので、ご提案の際はカンプ画像を利用いただき、採用後には素材のURL or ファイル番号をお伝えいただきます。

その他ご不明な点がございましたら、お気軽にご連絡下さい。
依頼公開後の追記内容
皆様短い期間の中大変多くの提案をいただきまことにありがとうございました。
ただいま、先方の企業様にて選定いただいている最中ですので、当選発表をお待ち下さい。
■ 選んだ理由

クライアント企業様から
「面白さという面では100%ではないが、熱を感じた。」
と評価いただきました。

■ 提案者全員のお礼・コメント

当選のご連絡が大変遅くなりまして申し訳ございませんでした。
クライアント企業様も、皆様から寄せられた案が秀逸で選定に相当悩んでおりましたが、この度決定いたしました。
多数採用したいところですが、苦渋の決断でした。
みなさま多数のご参加本当にありがとうございました。
この度選ばれなかった方も、機会がございましたらまたよろしくお願いいたします。

```html
<!DOCTYPE html>
<html lang="ja">
<head>
<meta charset="utf-8">
<title>HARUNE INDUSTRY</title>
<link rel="stylesheet" href="https://fonts.googleapis.com/css2?family=Montserrat:wght@400;500;600;700&family=Noto+Sans+JP:wght@400;500;700&family=Yellowtail&family=Klee+One:wght@600&display=swap">
<style>
:root{
  --navy:#17427a;
  --navy-deep:#123766;
  --pale:#dfe7f0;
  --pale-2:#d3dfea;
  --ink:#2b2f36;
  --grey:#8d939b;
  --green:#5fb38c;
  --white:#ffffff;
}
*{margin:0;padding:0;box-sizing:border-box}
html,body{width:1200px;height:4892px;overflow:hidden}
body{position:relative;background:var(--white);color:var(--ink);font-family:"Noto Sans JP",sans-serif}
.abs{position:absolute}
.script{font-family:"Yellowtail",cursive}
.btn{position:absolute;display:flex;align-items:center;justify-content:center;gap:14px;width:200px;height:44px;font-family:"Montserrat",sans-serif;font-size:12px;letter-spacing:.15em;font-weight:600}
.btn::after{content:"";width:28px;height:1px;background:currentColor}
.btn--outline{border:1px solid var(--navy);color:var(--navy)}
.btn--solid{background:var(--navy);color:var(--white)}
.btn--light{border:1px solid var(--white);color:var(--white)}

.hero{left:0;top:0;width:1200px;height:700px;background:linear-gradient(120deg,#7e8590 0%,#b9bec5 40%,#6f7782 100%)}
.brand{left:40px;top:34px;display:flex;align-items:center;gap:12px;color:var(--white);font-family:"Montserrat",sans-serif;font-weight:700;font-size:20px;letter-spacing:.08em}
.brand__dot{width:34px;height:34px;border-radius:50%;background:var(--navy)}
.nav{right:40px;top:36px;display:flex;gap:40px;align-items:center;font-family:"Montserrat",sans-serif;font-size:13px;font-weight:600;letter-spacing:.12em;color:var(--white)}
.nav__contact{background:var(--green);padding:8px 20px}
.hero__copy{left:0;width:1200px;top:292px;text-align:center;color:var(--white);font-size:92px;letter-spacing:.06em;white-space:nowrap}
.hero__scroll{right:44px;top:520px;writing-mode:vertical-rl;font-family:"Montserrat",sans-serif;font-size:11px;letter-spacing:.3em;color:var(--white)}
.hero__scroll::after{content:"";display:inline-block;height:60px;width:1px;background:var(--white);margin-top:12px}

.news{left:0;top:700px;width:760px;height:52px;background:var(--navy);color:var(--white);display:flex;align-items:center;gap:40px;padding-left:80px;font-size:13px}
.news__date{font-family:"Montserrat",sans-serif;letter-spacing:.08em}

.mission{left:0;top:830px;width:1200px;text-align:center}
.label{font-size:13px;font-weight:700;letter-spacing:.2em}
.heading{font-family:"Montserrat",sans-serif;font-weight:600;font-size:36px;letter-spacing:.12em}
.mission .label{color:var(--navy);margin-bottom:6px}
.mission .heading{color:var(--navy)}
.mission__sub{margin-top:60px;font-family:"Klee One",cursive;font-size:22px;letter-spacing:.3em;color:var(--ink)}
.mission__text{margin-top:58px;font-size:13px;line-height:2.3;letter-spacing:.08em}

.pale-band{left:0;top:1400px;width:1200px;height:2400px;background:var(--pale)}

.service__photo{left:88px;top:1460px;width:512px;height:400px;background:linear-gradient(135deg,#5b6470,#a6a9aa 55%,#c9a64a 80%,#6a6f74)}
.service__panel{left:600px;top:1490px;width:600px;height:470px;background:var(--navy);color:var(--white);text-align:center;padding-top:92px}
.service__panel .label{margin-bottom:6px}
.service__text{margin-top:40px;font-size:13px;line-height:2.1;letter-spacing:.06em}
.service__panel .btn{left:200px;top:368px}

.product1{left:0;top:2010px;width:960px;height:360px;background:var(--white)}
.product__num{font-size:64px;color:var(--pale-2);white-space:nowrap}
.product__title{font-size:24px;font-weight:700;color:var(--ink);letter-spacing:.06em}
.product__spec{font-size:13px;line-height:1.8;letter-spacing:.04em}
.product1__img{left:720px;top:2190px;width:480px;height:290px;background:var(--white)}
.ph-rollers{position:absolute;left:40px;top:40px;width:400px;height:210px;background:radial-gradient(ellipse at 50% 55%,#5a5e64 0%,#8b8f95 40%,#ffffff 72%)}
.product2__img{left:0;top:2660px;width:600px;height:320px;background:var(--white)}
.ph-pins{position:absolute;left:160px;top:40px;width:360px;height:240px;background:radial-gradient(ellipse at 50% 50%,#6b6f75 0%,#9a9ea4 40%,#ffffff 72%)}

.company{left:88px;top:3140px;width:1112px;height:520px;background:linear-gradient(180deg,rgba(23,66,122,.55),rgba(23,66,122,.75)),linear-gradient(120deg,#5c7a63,#7f98a8 50%,#3a4d6a)}
.company__body{left:160px;top:3265px;color:var(--white)}
.company__text{margin-top:40px;font-size:13px;line-height:2.1;letter-spacing:.06em}

.cta{top:3800px;width:600px;height:260px;padding:120px 0 0 110px}
.cta--contact{left:0;background:#d8e4ee}
.cta--recruit{left:600px;background:#cbdbe8;padding-left:90px}
.cta__title{font-family:"Montserrat",sans-serif;font-size:18px;font-weight:600;letter-spacing:.12em;color:var(--ink);display:flex;align-items:center;gap:20px}
.cta__title::after{content:"";width:280px;height:1px;background:var(--ink)}
.cta__sub{margin-top:14px;font-size:11px;color:var(--grey)}

.footer{left:0;top:4060px;width:1200px;height:400px;background:var(--navy);color:var(--white)}
.footer__slogan{left:88px;top:118px;font-size:26px;font-weight:700;line-height:1.6;letter-spacing:.06em}
.office{top:110px;font-size:11px;line-height:1.9;letter-spacing:.04em}
.office__name{font-size:15px;font-weight:700;margin-bottom:16px}
.footer__brand{left:88px;top:290px;display:flex;align-items:center;gap:10px;font-family:"Montserrat",sans-serif;font-weight:700;font-size:16px;letter-spacing:.08em}
.footer__brand span{width:26px;height:26px;border-radius:50%;background:var(--white)}
.footer__copy{left:88px;top:348px;font-size:10px;font-family:"Montserrat",sans-serif;letter-spacing:.06em;opacity:.8}
.footer__nav{right:88px;top:342px;display:flex;gap:36px;font-family:"Montserrat",sans-serif;font-size:12px;font-weight:600;letter-spacing:.12em}

.map{left:0;top:4460px;width:1200px;height:432px;background:linear-gradient(135deg,#e7e7e5,#d9dad6 50%,#ececea)}
.map__pin{left:560px;top:4560px;width:86px;height:86px;border-radius:50%;background:var(--navy)}
</style>
</head>
<body>

<div class="abs hero" role="img" aria-label="工場で機械を操作する作業者の写真"></div>
<div class="abs brand"><span class="brand__dot"></span>HARUNE INDUSTRY</div>
<nav class="abs nav"><span>COMPANY</span><span>SERVICE</span><span>RECRUIT</span><span class="nav__contact">CONTACT</span></nav>
<p class="abs hero__copy script">No Fun, No Manufacture</p>
<p class="abs hero__scroll">SCROLL</p>

<div class="abs news"><span class="news__date">2018.01.31</span><span>サイトリニューアルのお知らせ</span></div>

<section class="abs mission">
  <p class="label">理念</p>
  <h2 class="heading">OUR MISSION</h2>
  <p class="mission__sub">面白くなくっちゃ、ものづくりじゃない</p>
  <p class="mission__text">楽しくて面白い仕事をし、世界が驚くものをつくりたい。<br>困難を楽しみ、挑戦することをものづくりの原動力に、<br>アイデアと技術で未来を形にします。<br><br>職人の知恵と新しい発想をあわせ、ものをつくる人の熱を大切にします。<br>使う人の笑顔を思い浮かべながら、精度にこだわり続けます。<br>これが私たちのものづくりの姿勢です。</p>
</section>
<a class="btn btn--outline" style="left:500px;top:1280px">VIEW MORE</a>

<div class="abs pale-band"></div>

<div class="abs service__photo" role="img" aria-label="金属部品を加工する作業者の写真"></div>
<section class="abs service__panel">
  <p class="label">製品紹介</p>
  <h2 class="heading">SERVICE</h2>
  <p class="service__text">クロスローラー、円筒コロをはじめ、精密部品を製造します。<br>小ロットから量産まで、柔軟に対応しております。<br>特殊形状や難削材のご相談もお気軽にどうぞ。<br>海外からのご依頼にも、迅速に対応いたします。</p>
  <a class="btn btn--light">VIEW MORE</a>
</section>

<div class="abs product1"></div>
<p class="abs product__num script" style="left:140px;top:2030px">Product 01</p>
<h3 class="abs product__title" style="left:170px;top:2110px">クロスローラー、円筒コロ</h3>
<p class="abs product__spec" style="left:170px;top:2190px">径：1.5φ〜　長さ：1.5mm〜<br>真円度：1μm〜<br>面粗度：0.05Ra〜<br>外径公差：0.001μm Range〜</p>
<a class="btn btn--solid" style="left:170px;top:2348px">VIEW MORE</a>
<div class="abs product1__img"><div class="ph-rollers" role="img" aria-label="円筒コロ製品の写真"></div></div>

<p class="abs product__num script" style="left:600px;top:2520px">Product 02</p>
<h3 class="abs product__title" style="left:660px;top:2640px;line-height:1.5">モーターシャフト、歯車軸<br>ガイドピン、ピンゲージ</h3>
<p class="abs product__spec" style="left:760px;top:2740px">径：0.35φ〜　長さ：1.5mm〜<br>真円度：1μm〜<br>面粗度：0.05Ra〜<br>外径公差：0.001μm Range〜</p>
<a class="btn btn--solid" style="left:820px;top:2900px">VIEW MORE</a>
<div class="abs product2__img"><div class="ph-pins" role="img" aria-label="シャフトとピン製品の写真"></div></div>

<div class="abs company" role="img" aria-label="青空の下の工場建屋の写真"></div>
<section class="abs company__body">
  <p class="label">会社案内</p>
  <h2 class="heading">COMPANY</h2>
  <p class="company__text">会社案内文が入ります。会社案内文が入ります。会社案内文が入ります。<br>会社案内文が入ります。会社案内文が入ります。会社案内文が入ります。<br>会社案内文が入ります。会社案内文が入ります。</p>
</section>
<a class="btn btn--light" style="left:160px;top:3520px">VIEW MORE</a>

<div class="abs cta cta--contact"><p class="cta__title">CONTACT</p><p class="cta__sub">お問い合わせ</p></div>
<div class="abs cta cta--recruit"><p class="cta__title">RECRUIT</p><p class="cta__sub">求人情報</p></div>

<footer class="abs footer">
  <p class="abs footer__slogan">面白くなくっちゃ、<br>ものづくりじゃない</p>
  <div class="abs office" style="left:600px"><p class="office__name">東京本社</p><p>〒100-0000<br>東京都架空区見本町1-2-3<br>TEL 03-0000-1234<br>FAX 03-0000-1235</p></div>
  <div class="abs office" style="left:880px"><p class="office__name">秋田工場</p><p>〒010-0000<br>秋田県架空市工場通り4-5-6<br>TEL 018-000-5678<br>FAX 018-000-5679</p></div>
  <div class="abs footer__brand"><span></span>HARUNE INDUSTRY</div>
  <p class="abs footer__copy">©Harune Industry 2018. All Rights Reserved.</p>
  <nav class="abs footer__nav"><span>COMPANY</span><span>SERVICE</span><span>RECRUIT</span><span>CONTACT</span></nav>
</footer>

<div class="abs map" role="img" aria-label="工場周辺の地図"></div>
<div class="abs map__pin"></div>

</body>
</html>
```